Premium stylish simple clever card design for high end construction company.

I need a business card designed that is a standard size and shape (square edges) that is black in colour, with black edges. All text is to be either grey/silver or yellow/gold. On the front I want the logo (supplied as attachment g5) to be embossed or raised to give a texture. I also want the name of my company "The Kestrel Vault (larger font) construction co. (smaller font)" I like the clean style (found in attachment 56419286) of the black background with silver text. But the triangle is to be gold/yellow.

On the back needs to have my contact details. In silver or gold text.

Liam Porter - Builder
Liam@thekestrelvault.com.au
www.thekestrelvault.com.au
0427391065
Lic 517904k
PO BOX 739 Corrigan Bay NSW 2195

Must look simple, elegant and precise.

My work is of the utmost quality and my business card needs to project that. It needs to be simple and precise. It should scream luxury and confidence. Feel free to get creative with the font and font size. If you google "The Kestrel Vault" you will see it has links to great architecture, art, nature and the fibonacci sequence so i am open to using these ideas also.

Target Market(s)

High End home owners. 30-70 year olds.

Industry/Entity Type

Residential Construction

Contact Information for Business Card

Logo and company name on front. Contact details on back.

Font styles to use
Serif
Sans Serif

Colors
ffcf3e

Requirements
Must have
• black background
Nice to have
• debossed logo (silver and gold)
• debased company name (silver)
Should not have
• It should not look like a standard construction business card with pictures of hammers or tools etc.

```html
<!DOCTYPE html>
<html lang="en">
<head>
<meta charset="utf-8">
<title>The Kestrel Vault — Business Card</title>
<link rel="stylesheet" href="https://fonts.googleapis.com/css2?family=Open+Sans:wght@300;400;700&display=swap">
<style>
  :root {
    --stage: #1c1c1c;
    --card: #050505;
    --gold: #ffcf3e;
    --silver: #a9a9a9;
    --silver-light: #c8c8c8;
    --band-grey: #9b9b9b;
  }
  * { margin: 0; padding: 0; box-sizing: border-box; }
  html, body { width: 1200px; height: 659px; overflow: hidden; }
  body {
    background: var(--stage);
    font-family: "Open Sans", Arial, sans-serif;
    position: relative;
  }
  .card {
    position: absolute;
    width: 540px;
    height: 310px;
    background: var(--card);
    overflow: hidden;
  }
  .card svg.bands { position: absolute; inset: 0; }
  .card-front { left: 45px; top: 175px; }
  .card-back { left: 615px; top: 175px; }

  /* front */
  .front-lockup {
    position: absolute;
    left: 0; right: 0; top: 88px;
    display: flex; flex-direction: column; align-items: center;
  }
  .brand-row { display: flex; align-items: center; gap: 12px; }
  .brand-dot {
    width: 22px; height: 22px; border-radius: 50%;
    background: var(--gold);
  }
  .brand-name {
    font-weight: 300; font-size: 32px; letter-spacing: 1px;
    color: var(--silver-light); text-transform: uppercase;
  }
  .brand-sub {
    margin-top: 4px; margin-left: 34px;
    font-weight: 300; font-size: 11px; letter-spacing: 2px;
    color: var(--silver); text-transform: uppercase;
  }

  /* back */
  .back-lockup {
    position: absolute; right: 30px; top: 48px;
    display: flex; flex-direction: column; align-items: flex-end;
  }
  .back-lockup .brand-name { font-size: 19px; }
  .back-lockup .brand-dot { width: 14px; height: 14px; }
  .back-lockup .brand-row { gap: 8px; }
  .back-lockup .brand-sub { font-size: 7px; margin: 2px 0 0; }

  .gold-rule {
    position: absolute; left: 30px; right: 30px; top: 140px;
    height: 1px; background: var(--gold);
  }
  .person { position: absolute; left: 32px; top: 166px; }
  .person-name { font-weight: 700; font-size: 22px; color: var(--silver-light); line-height: 1.1; }
  .person-role { font-size: 12px; color: var(--gold); }

  .postal {
    position: absolute; left: 32px; top: 222px;
    font-size: 11px; line-height: 1.35; color: var(--silver);
  }
  .contacts {
    position: absolute; right: 16px; top: 152px;
    list-style: none; font-size: 11px; line-height: 1.55; color: var(--silver-light);
  }
  .contacts li { display: flex; align-items: center; justify-content: flex-end; gap: 6px; }
  .contacts svg { width: 11px; height: 11px; fill: var(--gold); }
</style>
</head>
<body>

<section class="card card-front" aria-label="Card front">
  <svg class="bands" viewBox="0 0 540 310" aria-hidden="true">
    <path d="M110,310 Q290,225 540,205 L540,228 Q320,250 150,310 Z" fill="var(--gold)"/>
  </svg>
  <div class="front-lockup">
    <div class="brand-row">
      <span class="brand-dot"></span>
      <span class="brand-name">The Kestrel Vault</span>
    </div>
    <span class="brand-sub">Construction Co</span>
  </div>
</section>

<section class="card card-back" aria-label="Card back">
  <svg class="bands" viewBox="0 0 540 310" aria-hidden="true">
    <path d="M0,168 L6,168 Q18,168 18,182 L18,262 Q18,280 36,280 L380,280 L380,310 L0,310 Z" fill="var(--gold)"/>
    <path d="M350,262 Q350,250 368,250 L540,250 L540,310 L350,310 Z" fill="var(--band-grey)"/>
  </svg>

  <div class="back-lockup">
    <div class="brand-row">
      <span class="brand-dot"></span>
      <span class="brand-name">The Kestrel Vault</span>
    </div>
    <span class="brand-sub">Construction Co</span>
  </div>

  <div class="gold-rule"></div>

  <div class="person">
    <div class="person-name">Liam Porter</div>
    <div class="person-role">Builder</div>
  </div>

  <address class="postal" style="font-style:normal">
    Lic 517904k<br>
    PO BOX 739<br>
    Corrigan Bay NSW 2195
  </address>

  <ul class="contacts">
    <li>0427391065
      <svg viewBox="0 0 24 24"><path d="M6.6 10.8a15 15 0 0 0 6.6 6.6l2.2-2.2c.3-.3.7-.4 1-.2 1.1.4 2.3.6 3.6.6.6 0 1 .4 1 1V20c0 .6-.4 1-1 1A17 17 0 0 1 3 4c0-.6.4-1 1-1h3.5c.6 0 1 .4 1 1 0 1.3.2 2.5.6 3.6.1.3 0 .7-.2 1z"/></svg>
    </li>
    <li>www.thekestrelvault.com.au
      <svg viewBox="0 0 24 24"><circle cx="12" cy="12" r="10"/><path d="M2 12h20M12 2c3 3 3 17 0 20M12 2c-3 3-3 17 0 20" stroke="#050505" stroke-width="1.6" fill="none"/></svg>
    </li>
    <li>Liam@thekestrelvault.com.au
      <svg viewBox="0 0 24 24"><rect x="2" y="5" width="20" height="14" rx="2"/><path d="M3 6l9 7 9-7" stroke="#050505" stroke-width="1.8" fill="none"/></svg>
    </li>
  </ul>
</section>

</body>
</html>
```